Silver Dart Shiners packaging design

We need a packaging design for Kestner Trailworks LLC. The Brand Name is Silver Dart Shiners, this is a fishing lure that was developed by a Inland Angling Honor Roll Society inductee. We would like to see the designs that use the color green in the packaging. the final design should represent quality. excitement and Innovation. The Package size is 3 inches wide and 4 inches tall, this will be a pegged package so the front of the package is all that will need to be designed.
Target Market(s)
age 25-55 Male and Female
Logo Text
Tough and represents quality
Requirements
Must have
- Silver Dart Shiners as logo
- Tagline Inspired a World Record Fishing Title
- Notes not what to say but have it represented in the design: Bold and strength contemporary and sharp
Nice to have
- na
Should not have
- na

```html
<!DOCTYPE html>
<html lang="en">
<head>
<meta charset="utf-8">
<title>Silver Dart Shiners – Peg Card Packaging</title>
<link href="https://fonts.googleapis.com/css2?family=Montserrat:wght@700;800&family=Oswald:wght@500&display=swap" rel="stylesheet">
<style>
  :root {
    --lime: #8cd600;
    --orange: #f57f00;
    --sky: #00a0dc;
    --ink: #0b0b0b;
    --paper: #ffffff;
    --window-shade: rgba(0, 0, 0, 0.09);
    --art-shade: rgba(11, 11, 11, 0.82);
  }
  html, body {
    margin: 0;
    padding: 0;
    width: 1200px;
    height: 1000px;
    overflow: hidden;
    background: var(--paper);
  }
  .stage {
    position: relative;
    width: 1200px;
    height: 1000px;
  }
  .wordmark {
    position: absolute;
    top: 228px;
    width: 318px;
    text-align: center;
    font-family: "Montserrat", sans-serif;
    font-weight: 800;
    font-size: 28px;
    line-height: 1;
    color: var(--accent);
    white-space: nowrap;
  }
  .peg-card {
    position: absolute;
    top: 335px;
    width: 318px;
    height: 425px;
    border-radius: 14px;
    overflow: hidden;
    background: var(--accent);
    box-shadow: 0 2px 8px rgba(0, 0, 0, 0.35);
  }
  .peg-card svg {
    display: block;
    width: 318px;
    height: 425px;
  }
  .variant-lime { --accent: var(--lime); }
  .variant-orange { --accent: var(--orange); }
  .variant-sky { --accent: var(--sky); }
  .col-1 { left: 87px; }
  .col-2 { left: 443px; }
  .col-3 { left: 799px; }

  .shape-ink { fill: var(--ink); }
  .line-accent { stroke: var(--accent); stroke-width: 2; }
  .hang-hole { fill: var(--paper); }
  .product-window { fill: var(--window-shade); }
  .art-area { fill: var(--art-shade); }
  .brand-name {
    font-family: "Montserrat", sans-serif;
    font-weight: 800;
    font-size: 23px;
    fill: var(--accent);
  }
  .tagline {
    font-family: "Oswald", sans-serif;
    font-weight: 500;
    font-size: 9.5px;
    font-style: italic;
    fill: var(--accent);
    text-transform: uppercase;
    letter-spacing: 0.2px;
  }
  .maker-name {
    font-family: "Montserrat", sans-serif;
    font-weight: 700;
    font-size: 12.5px;
    fill: var(--paper);
    letter-spacing: 1.6px;
  }
</style>
</head>
<body>
<main class="stage">

  <div class="wordmark variant-lime col-1">Silver Dart Shiners</div>
  <div class="wordmark variant-orange col-2">Silver Dart Shiners</div>
  <div class="wordmark variant-sky col-3">Silver Dart Shiners</div>

  <section class="peg-card variant-lime col-1" aria-label="Silver Dart Shiners card, green">
    <svg viewBox="0 0 318 425" xmlns="http://www.w3.org/2000/svg">
      <rect class="shape-ink" x="0" y="0" width="40" height="425"/>
      <rect class="shape-ink" x="0" y="78" width="318" height="50"/>
      <line class="line-accent" x1="0" y1="78" x2="40" y2="78"/>
      <line class="line-accent" x1="40" y1="138" x2="0" y2="186"/>
      <rect class="hang-hole" x="120" y="44" width="104" height="22" rx="11"/>
      <circle class="hang-hole" cx="172" cy="44" r="10"/>
      <text class="brand-name" x="20" y="112">Silver Dart Shiners</text>
      <rect class="shape-ink" x="127" y="140" width="191" height="15"/>
      <text class="tagline" x="134" y="151">Inspired a World Record Fishing Title</text>
      <rect class="product-window" x="48" y="181" width="220" height="202" rx="10"/>
      <rect class="art-area" role="img" aria-label="Illustration of a leaping bass in dark tones with accent highlights" x="145" y="240" width="173" height="185" rx="12"/>
      <text class="maker-name" transform="translate(27 400) rotate(-90)">KESTNER TRAILWORKS L.L.C.</text>
    </svg>
  </section>

  <section class="peg-card variant-orange col-2" aria-label="Silver Dart Shiners card, orange">
    <svg viewBox="0 0 318 425" xmlns="http://www.w3.org/2000/svg">
      <rect class="shape-ink" x="0" y="0" width="40" height="425"/>
      <rect class="shape-ink" x="0" y="78" width="318" height="50"/>
      <line class="line-accent" x1="0" y1="78" x2="40" y2="78"/>
      <line class="line-accent" x1="40" y1="138" x2="0" y2="186"/>
      <rect class="hang-hole" x="120" y="44" width="104" height="22" rx="11"/>
      <circle class="hang-hole" cx="172" cy="44" r="10"/>
      <text class="brand-name" x="20" y="112">Silver Dart Shiners</text>
      <rect class="shape-ink" x="127" y="140" width="191" height="15"/>
      <text class="tagline" x="134" y="151">Inspired a World Record Fishing Title</text>
      <rect class="product-window" x="48" y="181" width="220" height="202" rx="10"/>
      <rect class="art-area" role="img" aria-label="Illustration of a leaping bass in dark tones with accent highlights" x="145" y="240" width="173" height="185" rx="12"/>
      <text class="maker-name" transform="translate(27 400) rotate(-90)">KESTNER TRAILWORKS L.L.C.</text>
    </svg>
  </section>

  <section class="peg-card variant-sky col-3" aria-label="Silver Dart Shiners card, blue">
    <svg viewBox="0 0 318 425" xmlns="http://www.w3.org/2000/svg">
      <rect class="shape-ink" x="0" y="0" width="40" height="425"/>
      <rect class="shape-ink" x="0" y="78" width="318" height="50"/>
      <line class="line-accent" x1="0" y1="78" x2="40" y2="78"/>
      <line class="line-accent" x1="40" y1="138" x2="0" y2="186"/>
      <rect class="hang-hole" x="120" y="44" width="104" height="22" rx="11"/>
      <circle class="hang-hole" cx="172" cy="44" r="10"/>
      <text class="brand-name" x="20" y="112">Silver Dart Shiners</text>
      <rect class="shape-ink" x="127" y="140" width="191" height="15"/>
      <text class="tagline" x="134" y="151">Inspired a World Record Fishing Title</text>
      <rect class="product-window" x="48" y="181" width="220" height="202" rx="10"/>
      <rect class="art-area" role="img" aria-label="Illustration of a leaping bass in dark tones with accent highlights" x="145" y="240" width="173" height="185" rx="12"/>
      <text class="maker-name" transform="translate(27 400) rotate(-90)">KESTNER TRAILWORKS L.L.C.</text>
    </svg>
  </section>

</main>
</body>
</html>
```